Tall ridge firewood

It a new firewood outlet in Jindabyne nsw that will only sell top hardwood firewood (ironbark , red gum, grey gum, an box mix. I would like to see a web page the we can do order online payment for delivery. It will all so need to have photos of the firewood. I all so have logo for tall ridge firewood
Must have a modem look but easy to use I would like to see a black back ground of some sort.

Here are some other firewood web pages for ideas and firewood info
http://www.kestrelfirewood.example.au
http://www.dunmorefirewood.example.au
http://www.wrenlogfirewood.example.au
http://www.tallisbluelogs.example.au/firewood

```html
<!DOCTYPE html>
<html lang="en">
<head>
<meta charset="utf-8">
<title>Tall ridge firewood</title>
<link href="https://fonts.googleapis.com/css2?family=PT+Sans:wght@400;700&family=Questrial&display=swap" rel="stylesheet">
<style>
:root{
  --blue:#1a6fb8;
  --charcoal:#3a3a3a;
  --page:#efeded;
  --panel:#f5f5f5;
  --ink:#333;
  --muted:#666;
  --line:#dcdcdc;
  --white:#fff;
}
*{box-sizing:border-box;margin:0;padding:0}
html,body{width:1200px;height:1070px;overflow:hidden}
body{position:relative;background:var(--page);font-family:"PT Sans",sans-serif;color:var(--ink)}
.abs{position:absolute}
.site-header{left:0;top:0;width:1200px;height:77px;background:var(--white)}
.brand{left:302px;top:22px;display:flex;align-items:center;gap:7px}
.brand-dot{width:14px;height:14px;border-radius:50%;background:var(--blue)}
.brand-name{font-weight:700;font-size:13px;color:var(--blue);text-transform:uppercase;letter-spacing:.2px}
.hotline{left:709px;top:29px;display:flex;gap:8px;align-items:flex-start}
.hotline-title{font-weight:700;font-size:10.5px;color:#444}
.hotline-numbers{font-size:8px;color:var(--muted);margin-top:3px}
.hotline-numbers b{font-weight:400;color:var(--blue)}
.hero{left:0;top:77px;width:1200px;height:293px;
  background:radial-gradient(ellipse at 55% 45%,#ffb347 0%,#f05a22 22%,#a8261a 45%,#3a1c14 75%,#2a1a14 100%)}
.hero-caption{left:286px;top:164px;width:356px;height:49px;background:#0b0b0b;color:#fff;
  font-family:"Questrial",sans-serif;font-size:13.5px;line-height:16px;padding:8px 13px}
.footer-band{left:0;top:972px;width:1200px;height:98px;background:var(--charcoal)}
.sheet{left:286px;top:288px;width:654px;height:725px;background:var(--white);box-shadow:0 2px 8px rgba(0,0,0,.12);border-radius:4px}
.nav{left:286px;top:288px;width:654px;height:37px;background:var(--blue);display:flex;border-radius:4px 4px 0 0;overflow:hidden}
.nav a{color:#fff;text-decoration:none;font-weight:700;font-size:8px;line-height:37px;padding:0 16px}
.nav a.current{background:var(--charcoal);padding:0 21px}
.sidebar{left:701px;top:325px;width:239px;height:413px;background:var(--panel)}
h2.section{font-weight:400;font-size:10.5px;color:#222;text-transform:uppercase;letter-spacing:.2px}
p.copy{font-size:7.6px;line-height:10px;color:var(--muted)}
p.copy a,.link{color:var(--blue);font-weight:700;text-decoration:none}
.photo-logs{left:307px;top:400px;width:168px;height:133px;
  background:linear-gradient(135deg,#c9a47e 0%,#8a6444 45%,#4a3324 100%)}
.bullet{left:716px;display:flex;gap:9px;width:200px}
.bullet svg{flex:none;margin-top:2px}
.divider{height:1px;background:var(--line)}
.delivery-cta{left:717px;top:514px;width:203px;height:40px;background:var(--blue);color:#fff;
  font-weight:700;font-size:9.5px;line-height:14.5px;text-align:center;padding-top:6px}
.rates{font-size:7.6px;line-height:10px;color:#333}
.order-btn{left:776px;top:667px;width:78px;height:29px;background:var(--charcoal);border:2px solid var(--blue);
  border-radius:7px;color:#fff;font-weight:700;font-size:7.5px;text-align:center;line-height:25px}
.info-band{left:307px;top:790px;width:613px;height:182px;background:var(--blue)}
.info-band h3{font-size:9.5px;font-weight:700;color:#fff;text-transform:uppercase}
.info-band p{font-size:7.6px;line-height:10px;color:#fff}
.info-band .more{color:#fff;font-style:italic;text-decoration:underline;font-size:7.6px}
.payments{left:636px;top:835px;width:256px;height:115px;background:#fff;padding:17px 0 0 17px;
  display:grid;grid-template-columns:repeat(8,21px);grid-auto-rows:15px;column-gap:10px;row-gap:17px}
.card{width:21px;height:15px;border-radius:2px;box-shadow:0 1px 2px rgba(0,0,0,.25)}
.contact-bar{left:306px;top:986px;display:flex;align-items:baseline;gap:14px;font-size:10.5px;color:#333}
.contact-bar .label{text-transform:uppercase}
.contact-bar .call{font-weight:700;font-size:13px;color:#888}
.footer-note{left:0;width:1200px;text-align:center;color:#ddd;font-size:6.3px;line-height:9.5px}
</style>
</head>
<body>
<header class="site-header abs">
  <div class="brand abs"><span class="brand-dot"></span><span class="brand-name">Tall ridge firewood</span></div>
  <div class="hotline abs">
    <svg width="24" height="24" viewBox="0 0 24 24"><circle cx="12" cy="12" r="12" fill="#111"/><path d="M8.6 6.5l2 2.3-1.1 1.3c.8 1.6 2 2.8 3.5 3.5l1.3-1.1 2.3 2-1 1.9c-4-.4-7.6-4-8-8z" fill="#fff"/></svg>
    <div>
      <div class="hotline-title">We're here for you</div>
      <div class="hotline-numbers">Phone <b>1.800.555.0142</b> (U.S.) | International <b>+1.805.555.0187</b></div>
    </div>
  </div>
</header>

<div class="hero abs" role="img" aria-label="Photo of hardwood logs burning in an open fireplace"></div>
<div class="hero-caption abs">Lorem ipsum dolor sit amet, consectetur adipisicing elit, sed do eiusmod tempor incididunt</div>

<div class="footer-band abs"></div>
<div class="sheet abs"></div>
<nav class="nav abs">
  <a class="current" href="#">HOME</a><a href="#">ORDER ONLINE</a><a href="#">WHY CHOOSE US</a><a href="#">CONTACT US</a>
</nav>
<aside class="sidebar abs"></aside>

<h2 class="section abs" style="left:307px;top:371px">Welcome to our website</h2>
<div class="photo-logs abs" role="img" aria-label="Photo of stacked hollow hardwood firewood logs"></div>
<p class="copy abs" style="left:488px;top:398px;width:200px">Lorem ipsum dolor sit amet, consectetur adipisicing elit, sed do eiusmod tempor incididunt ut labore et dolore magna aliqua. Ut enim ad minim veniam, quis nostrud exercitation ullamco laboris nisi ut aliquip ex ea commodo consequat. Duis aute irure dolor in reprehenderit in voluptate velit esse cillum dolore eu fugiat nulla pariatur. Excepteur sint occaecat cupidatat non proident, sunt in culpa qui officia deserunt mollit anim id est laborum.</p>
<p class="copy abs" style="left:488px;top:496px;width:200px">Lorem ipsum dolor sit amet, consectetur adipisicing elit, sed do eiusmod tempor incididunt ut labore et dolore magna aliqua. Ut enim ad minim veniam, quis nostrud exercitation ullamco laboris nisi ut aliquip ex ea commodo consequat.</p>
<p class="copy abs" style="left:307px;top:552px;width:382px">Lorem ipsum dolor sit amet, consectetur adipisicing elit, sed do eiusmod tempor incididunt ut labore et dolore magna aliqua. Ut enim ad minim veniam, quis nostrud exercitation ullamco laboris nisi ut aliquip ex ea commodo consequat. Duis aute irure dolor in reprehenderit in voluptate velit esse cillum dolore eu fugiat nulla pariatur. Excepteur sint occaecat cupidatat non proident, sunt in culpa qui officia deserunt mollit anim id est laborum.</p>

<h2 class="section abs" style="left:307px;top:616px">Why choose us</h2>
<p class="copy abs" style="left:307px;top:643px;width:382px">Lorem ipsum dolor sit amet, consectetur adipisicing elit, sed do <a href="#">eiusmod tempor</a> incididunt ut labore et dolore magna aliqua.</p>
<p class="copy abs" style="left:307px;top:676px;width:382px">Lorem ipsum dolor sit amet, consectetur adipisicing elit, sed do eiusmod tempor <a href="#">incididunt ut labore</a> et dolore magna aliqua.</p>
<p class="copy abs" style="left:307px;top:710px;width:382px">Lorem ipsum dolor sit amet, consectetur adipisicing elit, sed do <a href="#">eiusmod tempor</a> incididunt ut labore et dolore magna aliqua.</p>

<h2 class="section abs" style="left:717px;top:371px">Buying for us</h2>
<div class="bullet abs" style="top:398px">
  <svg width="10" height="10" viewBox="0 0 10 10"><path d="M1 1l3 4-3 4M5 1l3 4-3 4" fill="none" stroke="#bbb" stroke-width="1.4"/></svg>
  <p class="copy">Lorem ipsum dolor sit amet, consectetur adipisicing elit, sed do eiusmod tempor <a href="#">incididunt ut labore</a> et dolore magna aliqua.</p>
</div>
<div class="bullet abs" style="top:441px">
  <svg width="10" height="10" viewBox="0 0 10 10"><path d="M1 1l3 4-3 4M5 1l3 4-3 4" fill="none" stroke="#bbb" stroke-width="1.4"/></svg>
  <p class="copy">Lorem ipsum dolor sit amet, consectetur adipisicing elit, sed do <a href="#">eiusmod tempor</a> incididunt ut labore et dolore magna aliqua.</p>
</div>
<div class="divider abs" style="left:717px;top:491px;width:205px"></div>
<div class="delivery-cta abs">Delivery - Order Online Here<br>Or phone us on (02) 5550 1234</div>
<p class="rates abs" style="left:717px;top:569px;width:205px">We sell Premium Seasoned Ironbark and it is sold for delivery at the following rates:</p>
<p class="rates abs" style="left:717px;top:600px;width:205px">1/2 Ton / 1m3 &nbsp;- $279<br>1 Ton / &nbsp;&nbsp;2m3 &nbsp;- $439<br>2 Ton / &nbsp;&nbsp;4m3 &nbsp;- $850</p>
<p class="rates abs" style="left:717px;top:638px;width:205px">Delivery charges do apply. Please <span class="link">Click Here</span> for delivery rates.</p>
<div class="order-btn abs">ORDER ONLINE</div>
<div class="divider abs" style="left:717px;top:715px;width:205px"></div>

<section class="info-band abs">
  <h3 class="abs" style="left:19px;top:24px">About us</h3>
  <p class="abs" style="left:19px;top:48px;width:285px">Lorem ipsum dolor sit amet, consectetur adipisicing elit, sed do eiusmod tempor incididunt ut labore et dolore magna aliqua. Ut enim ad minim veniam, quis nostrud exercitation ullamco laboris nisi ut aliquip ex ea commodo consequat. Duis aute irure dolor in reprehenderit in voluptate velit esse cillum dolore eu fugiat nulla pariatur. Excepteur sint occaecat cupidatat non proident, sunt in culpa qui officia deserunt mollit anim id est laborum.</p>
  <a class="more abs" style="left:19px;top:129px" href="#">continue&gt;&gt;</a>
  <h3 class="abs" style="left:330px;top:24px">Payment option</h3>
</section>
<div class="payments abs" aria-label="Accepted payment methods">
  <span class="card" style="background:#d8dce6"></span><span class="card" style="background:#e8c9a8"></span><span class="card" style="background:#d6e2ef"></span><span class="card" style="background:#3b7fc4"></span><span class="card" style="background:#f2c94c"></span><span class="card" style="background:#9b59b6"></span><span class="card" style="background:#e3e3e3"></span><span class="card" style="background:#1f3d7a"></span>
  <span class="card" style="background:#2c6fb5"></span><span class="card" style="background:#5a8fd6"></span><span class="card" style="background:#e6dccf"></span><span class="card" style="background:#3fa3d8"></span><span class="card" style="background:#222"></span><span class="card" style="background:#1d8a5b"></span><span class="card" style="background:#e9d7d0"></span><span class="card" style="background:#e4e8ee"></span>
  <span class="card" style="background:#e6e8ee"></span><span class="card" style="background:#4f8fd1"></span><span class="card" style="background:#eeeeee"></span><span class="card" style="background:#e4e4e4"></span><span class="card" style="background:#e6e6e6"></span><span class="card" style="background:#dfe5ef"></span><span class="card" style="background:#e9e9e9"></span>
</div>

<div class="contact-bar abs">
  <span class="label">Contact us:</span>
  <span>Address Line Here, Lorem ipsum dolor sit amet, <span style="color:var(--blue)">consectetur adipisicing elit</span></span>
  <span class="call">Call: 12345 678900</span>
</div>
<p class="footer-note abs" style="top:1029px">Lorem ipsum dolor sit amet, consectetur adipisicing elit, sed do eiusmod tempor incididunt ut labore et dolore magna aliqua.<br>Ut enim ad minim veniam</p>
<p class="footer-note abs" style="top:1054px">All right reserved 2014</p>
</body>
</html>
```